Social Media Graphics - Harbor Climb REVISED

Create 6-7 individual social media graphics (square size) to encourage folks to join our online course called:

The Lantern Ledger Plan
How to Launch a Multi-Million Business From Scratch
Sign Up Today!

IMPORTANT: Make the largest and most prominent text on the graphic be: How to Launch a Multi-Million Business From Scratch

For the color scheme of the graphics, let's try a blue color palette; make sure the graphics appeal to both men and women

Make sure each graphic contains 1 of the 3 pics attached (crop pic as needed); and make sure one of the graphics is all TEXT only.

Target Market(s)

men and women looking to start a business

Industry/Entity Type

Entrepreneurship

Colors
0054AA
0677BA
7BADD7
CADEEF
E8F1F8

Requirements
Must have
• All the text and use the 3 pics provided; one graphic can be all text; Simple, modern design that's easy to read

```html
<!DOCTYPE html>
<html lang="en">
<head>
<meta charset="utf-8">
<title>Harbor Climb — Social Graphics</title>
<link href="https://fonts.googleapis.com/css2?family=Arimo:wght@400;700&family=Oswald:wght@400;500&display=swap" rel="stylesheet">
<style>
  :root {
    --orange: #e8703a;
    --orange-dark: #b9542a;
    --ink: #111111;
    --gold: #d9b44a;
    --navy: #1e3557;
    --steel: #2d5a8c;
    --sky-dark: #1f4f86;
    --sky-light: #9cc0e6;
    --green: #3a9540;
    --teal: #0098a8;
    --ice: #eef6fc;
    --purple: #9b63c4;
    --plum: #2a1d3a;
    --sand: #f1ece0;
    --red: #a8172a;
    --white: #ffffff;
  }
  * { margin: 0; padding: 0; box-sizing: border-box; }
  html, body { width: 1200px; height: 1000px; overflow: hidden; background: var(--white); }
  body { position: relative; font-family: "Arimo", Arial, sans-serif; }

  .tile { position: absolute; width: 354px; height: 354px; overflow: hidden; }
  .col-1 { left: 57px; } .col-2 { left: 423px; } .col-3 { left: 789px; }
  .row-1 { top: 138px; } .row-2 { top: 507px; }

  .abs { position: absolute; }
  .brand { position: absolute; white-space: nowrap; font-weight: 700; text-align: center; }
  .btn {
    position: absolute; display: flex; align-items: center; justify-content: center;
    background: var(--orange); color: var(--white); font-weight: 700; border-radius: 8px;
  }
  .photo { position: absolute; }

  /* Tile 1 — black */
  .t-black { background: var(--ink); }
  .t-black .brand { left: 0; width: 354px; top: 76px; font-size: 15px; color: var(--gold); }
  .t-black .headline {
    position: absolute; right: 48px; top: 168px; text-align: right;
    color: var(--white); font-size: 32.5px; line-height: 28.5px;
  }
  .t-black .btn { left: 165px; top: 299px; width: 139px; height: 23px; font-size: 14px; border-radius: 7px; }

  /* Tile 2 — blue sky */
  .t-sky { background: linear-gradient(160deg, var(--sky-dark) 0%, var(--sky-light) 45%, #dfeaf6 75%, var(--white) 100%); }
  .t-sky .card { left: 21px; top: 41px; width: 170px; height: 196px; background: var(--white); border-radius: 8px 8px 0 0; }
  .t-sky .lead { left: 37px; top: 60px; font-size: 33px; font-weight: 700; color: var(--ink); letter-spacing: -1px; }
  .t-sky .headline { left: 38px; top: 95px; font-size: 24px; line-height: 24px; color: var(--steel); letter-spacing: -0.5px; }
  .t-sky .band { left: 0; top: 237px; width: 146px; height: 54px; background: var(--steel); }
  .t-sky .photo { left: 184px; top: 130px; width: 170px; height: 224px;
    background: linear-gradient(180deg, #c9d7e6 0%, #8a5a4a 40%, #d6324f 75%, #2a2626 100%); border-radius: 50px 50px 0 0; }
  .t-sky .brand { left: 212px; top: 58px; width: 124px; font-size: 12px; line-height: 14px; color: var(--red); white-space: normal; }
  .t-sky .bar { left: 0; top: 316px; width: 354px; height: 20px; background: var(--orange); }
  .t-sky .bar-text { left: 28px; top: 318px; color: var(--white); font-weight: 700; font-size: 13px; }

  /* Tile 3 — green */
  .t-green { background: radial-gradient(circle at 50% 50%, var(--green) 45%, #5e8f61 75%, #9aa89a 100%); }
  .t-green .frame { left: 73px; top: 61px; width: 208px; height: 224px; border: 1px solid var(--gold); border-radius: 10px; }
  .t-green .brand-gap { left: 100px; top: 50px; width: 154px; height: 22px; background: var(--green); }
  .t-green .brand { left: 0; width: 354px; top: 54px; font-size: 11px; color: var(--white); }
  .t-green .headline {
    left: 95px; top: 92px; font-family: "Oswald", "Arial Narrow", sans-serif; font-weight: 400;
    color: var(--white); font-size: 31px; line-height: 28.5px;
  }
  .t-green .btn { left: 95px; top: 222px; width: 161px; height: 36px; background: var(--ink); font-size: 17px; border-radius: 8px; }

  /* Tile 4 — ice / purple */
  .t-ice { background: var(--ice); }
  .t-ice .brand { left: 0; width: 354px; top: 24px; font-size: 9px; color: var(--orange-dark); }
  .t-ice .headline {
    left: 0; width: 354px; top: 45px; text-align: center; color: var(--steel);
    font-size: 18px; line-height: 16px;
  }
  .t-ice svg.wave { position: absolute; left: 0; top: 110px; }
  .t-ice .photo { left: 57px; top: 100px; width: 240px; height: 211px;
    background: linear-gradient(180deg, #7a5040 0%, #2a2a2a 45%, #1f3b6e 100%); border-radius: 90px 90px 0 0; }
  .t-ice .base { left: 0; top: 311px; width: 354px; height: 43px; background: linear-gradient(180deg, #3a2855, var(--plum)); }
  .t-ice .ribbon-end { top: 296px; width: 40px; height: 34px; background: var(--orange-dark); border-radius: 14px 14px 0 0; }
  .t-ice .btn { left: 63px; top: 296px; width: 228px; height: 50px; font-size: 25px; border-radius: 0 0 14px 14px; }

  /* Tile 5 — teal text only */
  .t-teal { background: var(--teal); }
  .t-teal .brand { left: 0; width: 354px; top: 84px; font-size: 12px; color: var(--white); }
  .t-teal .headline {
    left: 0; width: 354px; top: 126px; text-align: center; color: var(--white);
    font-size: 32.5px; line-height: 28px;
  }
  .t-teal .btn { left: 120px; top: 256px; width: 112px; height: 24px; font-size: 12px; }

  /* Tile 6 — sand */
  .t-sand { background: var(--sand); }
  .t-sand .photo { left: 0; top: 95px; width: 260px; height: 259px;
    background: linear-gradient(100deg, #8a8478 0%, #2a3d66 30%, #6e6a62 55%, rgba(241,236,224,0) 100%); }
  .t-sand .brand { left: 20px; top: 46px; width: 140px; font-size: 12px; color: var(--navy); }
  .t-sand .headline {
    right: 21px; top: 52px; text-align: right; color: var(--ink);
    font-size: 23px; line-height: 20px;
  }
  .t-sand .tape {
    position: absolute; left: -30px; width: 420px; height: 19px; background: var(--ink);
    display: flex; justify-content: space-around; align-items: center;
    color: var(--white); font-weight: 700; font-size: 9px; white-space: nowrap;
  }
  .t-sand .tape-a { top: 295px; transform: rotate(13.5deg); }
  .t-sand .tape-b { top: 290px; transform: rotate(-12deg); }
</style>
</head>
<body>

  <!-- Black -->
  <section class="tile col-1 row-1 t-black">
    <div class="brand">The Lantern Ledger Plan</div>
    <h2 class="abs headline" style="font-weight:400">How to Launch a<br>Multi-Million<br>Business From<br>Scratch</h2>
    <div class="btn">Sign Up Today!</div>
  </section>

  <!-- Sky -->
  <section class="tile col-2 row-1 t-sky">
    <div class="abs card"></div>
    <div class="abs band"></div>
    <div class="abs lead">How to</div>
    <h2 class="abs headline" style="font-weight:400">Launch a<br>Multi-Million<br>Business<br>From<br>Scratch</h2>
    <div class="photo" role="img" aria-label="Two course hosts smiling, woman in red dress with arms crossed and man in black"></div>
    <div class="brand">The Lantern<br>Ledger Plan</div>
    <div class="abs bar"></div>
    <svg class="abs" style="left:0;top:0" width="354" height="354" aria-hidden="true">
      <path d="M150 336 C230 330 270 250 354 238 L354 250 C280 262 240 336 150 336 Z" fill="#e8703a" opacity="0.85"/>
    </svg>
    <div class="abs bar-text">Sign Up Today!</div>
  </section>

  <!-- Green -->
  <section class="tile col-3 row-1 t-green" role="img" aria-label="Green background scattered with hundred-dollar bills">
    <div class="abs frame"></div>
    <div class="abs brand-gap"></div>
    <div class="brand">The Lantern Ledger Plan</div>
    <h2 class="abs headline">How to Launch<br>a Multi-Million<br>Business From<br>Scratch</h2>
    <div class="btn">Sign Up Today!</div>
  </section>

  <!-- Ice / purple -->
  <section class="tile col-1 row-2 t-ice">
    <div class="brand">The Lantern Ledger Plan</div>
    <h2 class="abs headline" style="font-weight:400">How to Launch a<br>Multi-Million Business From<br>Scratch</h2>
    <svg class="wave" width="354" height="210" aria-hidden="true">
      <defs>
        <linearGradient id="purpleFade" x1="0" y1="0" x2="0" y2="1">
          <stop offset="0" stop-color="#c7a3e0"/>
          <stop offset="1" stop-color="#7d3fb0"/>
        </linearGradient>
      </defs>
      <path d="M0 12 C60 0 110 40 140 70 L214 70 C244 40 294 0 354 12 L354 90 L0 130 Z" fill="url(#purpleFade)"/>
    </svg>
    <div class="photo" role="img" aria-label="Course hosts standing together, man in black turtleneck and woman in blue denim jacket"></div>
    <div class="abs base"></div>
    <div class="abs ribbon-end" style="left:33px"></div>
    <div class="abs ribbon-end" style="left:281px"></div>
    <div class="btn">Sign Up Today!</div>
  </section>

  <!-- Teal, text only -->
  <section class="tile col-2 row-2 t-teal">
    <div class="brand">The Lantern Ledger Plan</div>
    <h2 class="abs headline" style="font-weight:400">How to Launch<br>a Multi-Million<br>Business From<br>Scratch</h2>
    <div class="btn">Sign Up Today!</div>
  </section>

  <!-- Sand -->
  <section class="tile col-3 row-2 t-sand">
    <div class="photo" role="img" aria-label="Hosts on stage, man speaking into a microphone beside woman in blue blazer"></div>
    <div class="brand">The Lantern Ledger Plan</div>
    <h2 class="abs headline" style="font-weight:400">How to<br>Launch a<br>Multi-Million<br>Business<br>From<br>Scratch</h2>
    <div class="tape tape-a"><span>Sign Up Today!</span><span>Sign Up Today!</span><span>Sign Up Today!</span><span>Sign Up Today!</span></div>
    <div class="tape tape-b"><span>Sign Up Today!</span><span>Sign Up Today!</span><span>Sign Up Today!</span><span>Sign Up Today!</span></div>
  </section>

</body>
</html>
```